Local Real Estate Office needs an innovative Letterhead Design

Using the attached Logo, please create a letterhead design that is innovative and unusual. I am looking for something that will appeal to young homebuyers as well as seniors going into Condos.

The attached logo for Marrowfield Hearth needs to be included (small but readable) as well as spaces for 2 agents "head shots" photos.
Updates

I need a spot on the letterhead for two photos (head shots). thx

Industry/Entity Type

Real Estate

```html
<!DOCTYPE html>
<html lang="en">
<head>
<meta charset="utf-8">
<title>Riverton Homes Letterhead</title>
<link href="https://fonts.googleapis.com/css2?family=Oswald:wght@600&family=Alegreya+Sans+SC:wght@500;700&display=swap" rel="stylesheet">
<style>
  :root {
    --navy: #1d2f66;
    --navy-deep: #15234f;
    --paper: #ffffff;
    --backdrop: #e9eaec;
    --ink: #1f2330;
    --photo-a: #b9a595;
    --photo-b: #3a3f4b;
  }
  * { margin: 0; padding: 0; box-sizing: border-box; }
  html, body { width: 1200px; height: 1200px; overflow: hidden; }
  body { background: var(--backdrop); position: relative; }

  .letterhead {
    position: absolute;
    left: 175px; top: 50px;
    width: 850px; height: 1100px;
    background: var(--paper);
    box-shadow: 0 6px 24px rgba(0,0,0,0.12);
    overflow: hidden;
  }

  .bands { position: absolute; inset: 0; width: 850px; height: 1100px; }
  .band { fill: var(--navy); }

  .brand {
    position: absolute; left: 44px; top: 62px;
    font-family: "Oswald", "Arial Narrow", sans-serif;
    font-weight: 600; font-size: 40px; letter-spacing: 0.5px;
    color: var(--navy); line-height: 1;
  }

  .partner {
    position: absolute; right: 160px; top: 156px;
    display: flex; align-items: center; gap: 8px;
    font-family: "Alegreya Sans SC", sans-serif;
    font-weight: 700; font-size: 17px; line-height: 1;
    color: var(--navy); white-space: nowrap;
  }
  .partner-square { width: 14px; height: 14px; background: var(--navy); flex: none; }

  .headshot {
    position: absolute;
    background: linear-gradient(180deg, var(--photo-a) 0%, var(--photo-a) 55%, var(--photo-b) 100%);
  }
  .headshot--senior { left: 705px; top: 112px; width: 125px; height: 150px; }
  .headshot--junior { left: 24px; top: 895px; width: 125px; height: 165px; }

  .agent-name {
    position: absolute;
    font-family: "Alegreya Sans SC", sans-serif;
    font-weight: 700; font-size: 21px; letter-spacing: 1.5px;
    color: var(--paper); white-space: nowrap; line-height: 1;
  }
  .agent-name--senior { right: 160px; top: 232px; transform: rotate(5deg); transform-origin: right center; }
  .agent-name--junior { left: 180px; top: 1034px; }

  .contact-line {
    position: absolute; right: 22px; top: 1003px;
    font-family: "Alegreya Sans SC", sans-serif;
    font-weight: 500; font-size: 11.5px; color: var(--ink);
    display: flex; gap: 10px; white-space: nowrap;
  }
  .contact-line b { font-weight: 700; }
  .contact-divider { border-left: 1.5px solid var(--ink); }
</style>
</head>
<body>
  <main class="letterhead">
    <svg class="bands" viewBox="0 0 850 1100" aria-hidden="true">
      <polygon class="band" points="0,150 850,228 850,272 0,196"/>
      <polygon class="band" points="0,1022 850,1014 850,1062 0,1072"/>
    </svg>

    <div class="brand">www.RivertonHomes.com</div>

    <div class="partner"><span class="partner-square"></span>Marrowfield Hearth</div>

    <div class="headshot headshot--senior" role="img" aria-label="Head shot of agent Harold Vance"></div>
    <div class="agent-name agent-name--senior">Harold Vance</div>

    <div class="headshot headshot--junior" role="img" aria-label="Head shot of agent Owen Carrick"></div>
    <div class="agent-name agent-name--junior">Owen Carrick</div>

    <div class="contact-line">
      <span><b>Address:</b> Harold Vance &amp; Associates 412-88th Street East Riverton, Saskatchewan S7K 2B4</span>
      <span><b>Phone:</b> 306-555-0142</span>
      <span class="contact-divider"></span>
      <span><b>Fax:</b> (306) 555-0187</span>
    </div>
  </main>
</body>
</html>
```